New Logo and Packaging label for Sweet Chilli Sauce

We need a Logo Design for our business based in Sydney, Australia named Brovantu, and for the first product to launch which will be a Sweet Chilli Sauce. The logo and design has to be scalable to be used for other product additions over time.

The product will be distributed predominantly through growers markets and the web.

We do need a label that goes around a 250ml glass bottle (picture attached) and measures:
15cm tall and
6cm diameter at the widest point

To be included but not be limited to:
‘Brovantu’ logo that is developed
Sweet Chilli Sauce

Hand Made in Australia

250mL

Shake well
Refrigerate after opening

A section for ingredients, bar code and nutrition label

Target Market(s)

Foodies

Industry/Entity Type

Food Production

Logo Text

BROVANTU

Colors

Designer to choose colors to be used in the design.

```html
<!DOCTYPE html>
<html lang="en">
<head>
<meta charset="utf-8">
<title>Brovantu Sweet Chilli Sauce – Label Design</title>
<link href="https://fonts.googleapis.com/css2?family=Bebas+Neue&family=Oswald:wght@500;600&family=Roboto:wght@400&display=swap" rel="stylesheet">
<style>
  :root {
    --page-bg: #ffffff;
    --ink: #1f1f1f;
    --sauce-dark: #2a2a2a;
    --brand-red: #c4161c;
    --red-deep: #8e1115;
    --red-bright: #ed1c24;
    --green-deep: #0b6b34;
    --green-light: #8dc63f;
    --label-grey: #e4e4e4;
    --label-light: #f7f7f7;
    --label-edge: #c9c9c9;
  }
  html, body {
    margin: 0;
    padding: 0;
    overflow: hidden;
  }
  body {
    width: 1200px;
    height: 1000px;
    background: var(--page-bg);
    position: relative;
    font-family: "Roboto", Arial, sans-serif;
    color: var(--ink);
  }
  .sheet-title {
    position: absolute;
    left: 48px;
    top: 42px;
    margin: 0;
    font-size: 40px;
    font-weight: 400;
    line-height: 1.1;
  }
  .sheet-size {
    position: absolute;
    left: 48px;
    top: 106px;
    margin: 0;
    font-size: 27px;
    line-height: 1.1;
  }
  .label {
    position: absolute;
    left: 428px;
    top: 92px;
    width: 334px;
    height: 834px;
    outline: 1px solid var(--label-edge);
  }
  .label svg { display: block; }
  .brand-name {
    font-family: "Oswald", sans-serif;
    font-weight: 600;
    font-size: 26px;
    fill: var(--brand-red);
    letter-spacing: 0.5px;
  }
  .title-main {
    font-family: "Bebas Neue", sans-serif;
    font-size: 118px;
  }
  .title-sub {
    font-family: "Bebas Neue", sans-serif;
    font-size: 84px;
    fill: var(--sauce-dark);
  }
  .volume {
    font-family: "Oswald", sans-serif;
    font-weight: 500;
    font-size: 26px;
    fill: #ffffff;
  }
  .small-print {
    font-family: "Oswald", sans-serif;
    font-weight: 500;
    font-size: 10.5px;
    fill: #ffffff;
  }
</style>
</head>
<body>
  <h1 class="sheet-title">Label Design</h1>
  <p class="sheet-size">w6 x h15 cm</p>

  <div class="label">
    <svg width="334" height="834" viewBox="0 0 334 834" xmlns="http://www.w3.org/2000/svg">
      <defs>
        <linearGradient id="bg-grey" x1="0" y1="0" x2="1" y2="1">
          <stop offset="0" stop-color="#d2d2d2"/>
          <stop offset="0.45" stop-color="var(--label-light)"/>
          <stop offset="1" stop-color="var(--label-grey)"/>
        </linearGradient>
        <linearGradient id="band-green" x1="0" y1="1" x2="1" y2="0">
          <stop offset="0" stop-color="var(--green-deep)"/>
          <stop offset="0.5" stop-color="var(--green-light)"/>
          <stop offset="1" stop-color="var(--green-light)"/>
        </linearGradient>
        <linearGradient id="band-red" x1="0" y1="0" x2="1" y2="1">
          <stop offset="0" stop-color="var(--red-deep)"/>
          <stop offset="0.6" stop-color="var(--brand-red)"/>
          <stop offset="1" stop-color="var(--red-bright)"/>
        </linearGradient>
        <linearGradient id="title-fill" x1="0" y1="0" x2="1" y2="0">
          <stop offset="0" stop-color="var(--green-deep)"/>
          <stop offset="0.44" stop-color="var(--green-light)"/>
          <stop offset="0.445" stop-color="var(--red-bright)"/>
          <stop offset="1" stop-color="var(--red-deep)"/>
        </linearGradient>
        <radialGradient id="chilli-tone" cx="0.55" cy="0.55" r="0.5">
          <stop offset="0" stop-color="#d8221f" stop-opacity="0.85"/>
          <stop offset="0.6" stop-color="#e0362a" stop-opacity="0.45"/>
          <stop offset="1" stop-color="#e0362a" stop-opacity="0"/>
        </radialGradient>
      </defs>

      <rect class="label-ground" width="334" height="834" fill="url(#bg-grey)"/>
      <path class="sheen" d="M0,560 C120,420 230,200 334,40 L334,0 L300,0 C220,170 110,380 0,500 Z" fill="#ffffff" opacity="0.45"/>
      <path class="sheen" d="M60,834 C170,620 270,300 334,120 L334,200 C280,380 200,640 110,834 Z" fill="#ffffff" opacity="0.35"/>

      <path class="band-green" d="M0,708 C150,692 300,470 334,286 L334,834 L0,834 Z" fill="url(#band-green)"/>
      <path class="band-red" d="M0,768 C170,748 312,530 334,318 L334,834 L0,834 Z" fill="url(#band-red)"/>

      <rect class="chilli-photo" role="img" aria-label="Photo of two glossy red chilli peppers with green stems, crossed"
            x="20" y="486" width="298" height="222" fill="url(#chilli-tone)"/>

      <text class="brand-name" x="167" y="58" text-anchor="middle">Brovantu</text>

      <text class="title-main" transform="translate(116,613) rotate(-90)" textLength="495" lengthAdjust="spacingAndGlyphs" fill="url(#title-fill)">SWEET CHILLI</text>
      <text class="title-sub" transform="translate(194,283) rotate(-90)" textLength="165" lengthAdjust="spacingAndGlyphs">SAUCE</text>

      <text class="volume" x="177" y="749" text-anchor="middle">250mL</text>
      <text class="small-print" x="166" y="774" text-anchor="middle" textLength="169" lengthAdjust="spacingAndGlyphs">Shake well <tspan fill="var(--green-light)">•</tspan> Refrigerate after opening</text>
      <text class="small-print" x="174" y="798" text-anchor="middle" textLength="222" lengthAdjust="spacingAndGlyphs">Ingredient: Dummy Text, Dummy Text, Dummy Text,</text>
      <text class="small-print" x="176" y="817" text-anchor="middle" textLength="114" lengthAdjust="spacingAndGlyphs">Dummy Text, Dummy Text.</text>
    </svg>
  </div>
</body>
</html>
```